Business Card Design for Tolvane Holdings

I need a business card designed for Tolvane Holdings. I would like basic contact info and would like the card to be a bit modern but not childish. We manage several companies so it needs to look very professional. Watermark is cool and a plan logo maybe offset on the other side but I will leave the design up to you. I would like to see both color and grey scale designs. This is my first time using Pixel Bazaar so hopefully we get some great results! Future projects available for the selected designer potentially.

Target Market(s)

Tolvane Holdings owns several companies serving the software, real estate and automotive industry

Industry/Entity Type

Business

Contact Information for Business Card

Gordon P. Lask
512.608.2247
gordon.p.lask@mailbrook.net

Font styles to use
Serif

Requirements
Must have
• contact information listed on card details
Nice to have
• I am open to letting you use your creative mind to design the best eye catching cards.

```html
<!DOCTYPE html>
<html lang="en">
<head>
<meta charset="utf-8">
<title>Tolvane Holdings – Business Card</title>
<link rel="stylesheet" href="https://fonts.googleapis.com/css2?family=Arimo:wght@400;700&display=swap">
<style>
  :root {
    --backdrop: #e4e6e8;
    --card-white: #ffffff;
    --brand-blue: #0096cc;
    --brand-navy: #2e4a8c;
    --ink: #111418;
  }
  html, body {
    margin: 0;
    padding: 0;
    width: 1200px;
    height: 586px;
    overflow: hidden;
    background: var(--backdrop);
    font-family: "Arimo", Arial, sans-serif;
  }
  .business-card {
    position: absolute;
    left: 150px;
    top: 35px;
    width: 900px;
    height: 516px;
    border-radius: 30px;
    overflow: hidden;
    background: var(--card-white);
  }
  .card-graphics {
    position: absolute;
    inset: 0;
    width: 100%;
    height: 100%;
  }
  .holder-name {
    position: absolute;
    right: 25px;
    top: 30px;
    margin: 0;
    font-size: 29px;
    font-weight: 700;
    color: var(--ink);
    letter-spacing: 0.3px;
  }
  .holder-title {
    position: absolute;
    right: 25px;
    top: 68px;
    margin: 0;
    font-size: 24px;
    font-weight: 400;
    color: var(--card-white);
  }
  .brand-lockup {
    position: absolute;
    left: 60px;
    top: 244px;
    display: flex;
    align-items: center;
    gap: 18px;
  }
  .brand-dot {
    width: 96px;
    height: 96px;
    border-radius: 50%;
    background: var(--brand-blue);
  }
  .brand-name {
    font-size: 36px;
    font-weight: 700;
    color: var(--brand-navy);
  }
  .contact-list {
    position: absolute;
    right: 58px;
    top: 376px;
    margin: 0;
    padding: 0;
    list-style: none;
  }
  .contact-item {
    display: flex;
    justify-content: flex-end;
    align-items: center;
    gap: 14px;
    height: 40px;
    margin-bottom: 21px;
    font-size: 26px;
    color: var(--ink);
  }
  .contact-icon {
    width: 26px;
    height: 26px;
    flex: none;
  }
</style>
</head>
<body>
  <section class="business-card">
    <svg class="card-graphics" viewBox="0 0 623 357" preserveAspectRatio="none" aria-hidden="true">
      <path class="top-band" fill="var(--brand-blue)" d="M0,0 H623 V246 C560,118 330,24 0,50 Z"/>
      <path class="accent-swoosh" fill="var(--brand-navy)" d="M36,57 C330,30 566,118 623,262 L623,280 C558,132 330,44 36,57 Z"/>
    </svg>

    <h1 class="holder-name">GORDON P. LASK</h1>
    <p class="holder-title">Managing Partner</p>

    <div class="brand-lockup">
      <span class="brand-dot"></span>
      <span class="brand-name">Tolvane Holdings</span>
    </div>

    <ul class="contact-list">
      <li class="contact-item">
        <span class="contact-text">512.608.2247</span>
        <svg class="contact-icon" viewBox="0 0 26 26" aria-label="Phone">
          <circle cx="13" cy="13" r="13" fill="var(--brand-blue)"/>
          <path fill="#fff" d="M6,10 C6,7 20,7 20,10 L18,12 L16,10.5 L10,10.5 L8,12 Z M8,13 H18 L19,18 H7 Z"/>
        </svg>
      </li>
      <li class="contact-item">
        <span class="contact-text">gordon.p.lask@mailbrook.net</span>
        <svg class="contact-icon" viewBox="0 0 26 26" aria-label="Email">
          <circle cx="13" cy="13" r="13" fill="var(--brand-blue)"/>
          <rect x="7" y="8.5" width="12" height="9" fill="#fff"/>
          <path d="M7,8.5 L13,13.5 L19,8.5" fill="none" stroke="var(--brand-blue)" stroke-width="1.3"/>
        </svg>
      </li>
    </ul>
  </section>
</body>
</html>
```